Business Card Design Project: Classically Trained Singer and Voice Teacher

I am a classically trained singer that performs in Opera and Musical Theater and also teaches private voice lessons in those fields. I am looking for a business card that I can give to casting directors and colleagues, as well as to people who are interested in taking voice lessons from me.

This is sort of like an actors business card so I want my headshot and name to be the main focus.

I was kind of thinking of having the business card be horizontal with my headshot photo on the front taking up roughly half and my information on the same side, and perhaps my name again on the back or some form of my initials. But I am totally open to other options for layout.I would prefer to have a double sided business card, but once again, its not essential.

I am looking for it to look and feel elegant artistic and professional, without looking feminine.

Because of the colors of my headshot I would imagine that it would be predominantly brown and white, but I am totally open to other approaches.feel totally free to crop my headshot so that it fits better into your overall design and layout.

It is highly likely that I will ask the winner of the design to create a flyer for marketing my voice lessons with a similar look.

If you have any questions or clarifications, please feel free to ask.

Target Market(s)

Opera and Musical theater casting directors, colleagues; potential voice lesson students

Industry/Entity Type

Marketing

Requirements
Must have
• These must feature prominently:
- (My Headshot (attached))
- Marlow Keaton (my name)

These dont need to be as prominent:
- Baritone
- Private Voice Teacher
- Opera and Musical Theater

Contact Info:
Phone: (530) 555-0147
Email: markeat@inboxly.example

Nice to have
• Double sided

```html
<!DOCTYPE html>
<html lang="en">
<head>
<meta charset="utf-8">
<title>Marlow Keaton – Business Card</title>
<link rel="stylesheet" href="https://fonts.googleapis.com/css2?family=Pinyon+Script&family=EB+Garamond:wght@400;500&display=swap">
<style>
  :root {
    --backdrop: #1d1d1f;
    --parchment-light: #e2cc9c;
    --parchment-mid: #d3b67f;
    --parchment-edge: #ad8a52;
    --ink: #3a2616;
    --ink-soft: #4a3220;
    --photo-light: #c9a47e;
    --photo-mid: #8a6342;
    --photo-dark: #4b3320;
  }

  * { margin: 0; padding: 0; box-sizing: border-box; }

  html, body {
    width: 1200px;
    height: 982px;
    overflow: hidden;
  }

  body {
    background: var(--backdrop);
    position: relative;
    font-family: "EB Garamond", Georgia, serif;
    color: var(--ink);
  }

  .card {
    position: absolute;
    left: 250px;
    width: 700px;
    height: 400px;
    overflow: hidden;
    background:
      radial-gradient(ellipse at 45% 45%, var(--parchment-light) 0%, var(--parchment-mid) 60%, var(--parchment-edge) 100%);
    box-shadow: 0 6px 24px rgba(0, 0, 0, 0.55);
  }

  .card--front { top: 62px; }
  .card--back  { top: 520px; }

  .halftone { position: absolute; }

  .card--front .halftone {
    left: 0;
    top: 60px;
    width: 400px;
    height: 340px;
    background: radial-gradient(ellipse at 30% 70%, rgba(184, 151, 95, 0.55) 0%, rgba(184, 151, 95, 0) 70%);
  }

  .card--back .halftone--corner {
    right: 0;
    top: 0;
    width: 230px;
    height: 170px;
    background: radial-gradient(ellipse at 100% 0%, rgba(110, 83, 51, 0.6) 0%, rgba(110, 83, 51, 0) 70%);
  }

  .card--back .halftone--base {
    left: 0;
    bottom: 0;
    width: 380px;
    height: 200px;
    background: radial-gradient(ellipse at 0% 100%, rgba(110, 83, 51, 0.65) 0%, rgba(110, 83, 51, 0) 70%);
  }

  /* front side */
  .headshot {
    position: absolute;
    right: 0;
    top: 0;
    width: 300px;
    height: 400px;
    background:
      radial-gradient(ellipse at 55% 35%, var(--photo-light) 0%, var(--photo-mid) 45%, var(--photo-dark) 100%);
  }

  .front-text {
    position: absolute;
    left: 44px;
    top: 0;
    width: 340px;
    height: 400px;
  }

  .name {
    position: absolute;
    left: 0;
    top: 70px;
    font-family: "Pinyon Script", cursive;
    font-size: 52px;
    font-weight: 400;
    color: var(--ink);
    white-space: nowrap;
  }

  .contact {
    position: absolute;
    left: 0;
    top: 190px;
    list-style: none;
    font-size: 28px;
    line-height: 1.3;
    color: var(--ink-soft);
    white-space: nowrap;
  }

  /* back side */
  .roles {
    position: absolute;
    left: 64px;
    top: 60px;
    list-style: none;
    font-size: 30px;
    line-height: 1.45;
    color: var(--ink);
  }

  .roles li {
    display: flex;
    align-items: center;
  }

  .roles li::before {
    content: "";
    width: 11px;
    height: 11px;
    border-radius: 50%;
    background: var(--ink);
    margin-right: 18px;
    flex: none;
  }
</style>
</head>
<body>

  <section class="card card--front" aria-label="Business card front">
    <div class="halftone" role="img" aria-label="Soft halftone dot texture"></div>
    <div class="headshot" role="img" aria-label="Headshot photograph of Marlow Keaton"></div>
    <div class="front-text">
      <h1 class="name">Marlow Keaton</h1>
      <ul class="contact">
        <li class="contact__phone">(530) 555-0147</li>
        <li class="contact__email">markeat@inboxly.example</li>
      </ul>
    </div>
  </section>

  <section class="card card--back" aria-label="Business card back">
    <div class="halftone halftone--corner" role="img" aria-label="Halftone dot texture in the corner"></div>
    <div class="halftone halftone--base" role="img" aria-label="Halftone dot texture along the lower edge"></div>
    <ul class="roles">
      <li>Baritone</li>
      <li>Private Voice Teacher</li>
      <li>Opera and Musical Theater</li>
    </ul>
  </section>

</body>
</html>
```